Promotional poster for a vintage motorcycle show.

Vertically oriented, based on 11 x 17 inch proportions

Though not to the exclusion of other design concepts, stylistically perhaps something evoking a vintage (early-mid 20th century) 2-3 color silk screen style event poster.

In addition to some sort of eyecatching, vintage / antique motorbike oriented graphic (preferably not Corwin Baxley based), the poster should include the following text and info:

3rd Annual Milo Quenby Vintage Motorcycle Show
Bordentown City, N.J.
October 1st (rain date Oct. 2nd)
11am-4pm

Presented in conjunction with the 27th Annual Thistlewood Fair

For further info, or to register your pre-1992 bike contact:
Marty@wheelvaultex.com or 555-204-8913

Sponsored by:
UptownHallowmereGuildway.com
Wheelvaultex.com

Must have
• See above project description
Nice to have
• See above project describtion

```html
<!DOCTYPE html>
<html lang="en">
<head>
<meta charset="utf-8">
<title>Milo Quenby Vintage Motorcycle Show</title>
<link rel="stylesheet" href="https://fonts.googleapis.com/css2?family=Staatliches&family=Bowlby+One&family=Lobster+Two:wght@700&display=swap">
<style>
  :root {
    --paper: #e8e1d6;
    --paper-shade: #cfc3b2;
    --ink: #3f2a22;
    --plate: #6e5448;
  }
  html, body {
    margin: 0;
    padding: 0;
    width: 874px;
    height: 1200px;
    overflow: hidden;
    background: var(--paper);
  }
  .poster {
    display: block;
    width: 874px;
    height: 1200px;
  }
  .poster-paper { fill: var(--paper); }
  .paper-grain { fill: var(--paper-shade); opacity: .45; }
  .poster-frame { fill: none; stroke: var(--ink); stroke-width: 10; }
  .title {
    font-family: "Staatliches", Impact, sans-serif;
    font-size: 240px;
    fill: var(--ink);
  }
  .show-arc {
    font-family: "Bowlby One", Impact, sans-serif;
    font-size: 44px;
    fill: var(--ink);
  }
  .emblem-art, .bike-art { fill: var(--plate); }
  .distressed { filter: url(#worn-ink); }
  .script {
    font-family: "Lobster Two", cursive;
    font-weight: 700;
    fill: var(--ink);
  }
  .script-xs { font-size: 18px; }
  .script-s { font-size: 22px; }
  .script-m { font-size: 36px; }
  .script-l { font-size: 46px; }
  .script-xl { font-size: 64px; }
  .sponsor-label { font-size: 12px; }
  .sponsor-links { font-size: 25px; }
  .rule { stroke: var(--ink); stroke-width: 2.5; }
</style>
</head>
<body>
<svg class="poster" viewBox="0 0 874 1200" xmlns="http://www.w3.org/2000/svg">
  <defs>
    <filter id="worn-ink" x="0" y="0" width="100%" height="100%">
      <feTurbulence type="fractalNoise" baseFrequency="0.09" numOctaves="3" seed="7" result="noise"/>
      <feColorMatrix in="noise" type="matrix" values="0 0 0 0 0  0 0 0 0 0  0 0 0 0 0  0 0 0 -2.6 1.7" result="holes"/>
      <feComposite in="SourceGraphic" in2="holes" operator="in"/>
    </filter>
    <filter id="paper-mottle" x="0" y="0" width="100%" height="100%">
      <feTurbulence type="fractalNoise" baseFrequency="0.012" numOctaves="3" seed="3" result="cloud"/>
      <feColorMatrix in="cloud" type="matrix" values="0 0 0 0 0  0 0 0 0 0  0 0 0 0 0  0 0 0 1.6 -0.6" result="mask"/>
      <feComposite in="SourceGraphic" in2="mask" operator="in"/>
    </filter>
    <path id="show-curve" d="M55,330 Q437,530 815,330"/>
  </defs>

  <rect class="poster-paper" x="0" y="0" width="874" height="1200"/>
  <rect class="paper-grain" x="0" y="0" width="874" height="1200" filter="url(#paper-mottle)"/>
  <rect class="poster-frame" x="30" y="29" width="810" height="1146" rx="14"/>

  <!-- headline -->
  <text class="title distressed" x="435" y="239" text-anchor="middle" textLength="730" lengthAdjust="spacingAndGlyphs">MILO QUENBY</text>

  <!-- anniversary emblem area -->
  <polygon class="emblem-art" points="170,244 704,244 560,352 314,352" role="img" aria-label="Winged round emblem reading 3rd Annual"/>

  <text class="show-arc distressed"><textPath href="#show-curve" startOffset="50%" text-anchor="middle">VINTAGE MOTORCYCLE SHOW</textPath></text>

  <!-- event details -->
  <text class="script script-xs" x="435" y="490" text-anchor="middle">Presented in conjunction with the 27th Annual Thistlewood Fair</text>
  <text class="script script-s" x="435" y="525" text-anchor="middle">on</text>

  <rect class="bike-art" x="79" y="536" width="172" height="80" rx="28" role="img" aria-label="Illustration of a vintage chopper motorcycle facing right"/>
  <rect class="bike-art" x="598" y="536" width="187" height="80" rx="28" role="img" aria-label="Illustration of a vintage chopper motorcycle facing left"/>

  <text class="script script-xl" x="425" y="600" text-anchor="middle">October 1<tspan font-size="28" dy="-28">st</tspan></text>
  <text class="script script-m" x="435" y="651" text-anchor="middle">(rain date Oct. 2<tspan font-size="18" dy="-15">nd</tspan><tspan dy="15">)</tspan></text>
  <text class="script script-l" x="435" y="732" text-anchor="middle">Bordentown City, N.J.</text>
  <text class="script script-l" x="435" y="798" text-anchor="middle">11am-4pm</text>

  <line class="rule" x1="83" y1="828" x2="789" y2="828"/>
  <line class="rule" x1="83" y1="836" x2="789" y2="836"/>

  <!-- registration -->
  <text class="script script-m" x="435" y="880" text-anchor="middle">For information or to</text>
  <text class="script script-l" x="435" y="941" text-anchor="middle">Register Your Pre-1992 Bike</text>
  <text class="script script-m" x="435" y="998" text-anchor="middle">contact Marty@wheelvaultex.com</text>
  <text class="script script-m" x="435" y="1052" text-anchor="middle">or 555-204-8913</text>

  <line class="rule" x1="83" y1="1068" x2="789" y2="1068"/>
  <line class="rule" x1="83" y1="1076" x2="789" y2="1076"/>

  <!-- sponsors -->
  <text class="script sponsor-label" x="177" y="1106">Sponsored by:</text>
  <text class="script sponsor-links" x="435" y="1141" text-anchor="middle">UptownHallowmereGuildway.com  |  Wheelvaultex.com</text>
</svg>
</body>
</html>
```